My company is all about art and painting people's walls, cars and everything you can imagine, I would like a sharp professional buisness card which still has a good creative element

Industry/Entity Type

Painting

Contact Information for Business Card

Ka Tivo Art
Canvass,Murals,Vehicles,Cover art and tattoo design
Commissions available..
Www.pixelmeet.com/valdipe

```html
<!DOCTYPE html>
<html lang="en">
<head>
<meta charset="utf-8">
<title>Ka Tivo Art – Business Card</title>
<link rel="stylesheet" href="https://fonts.googleapis.com/css2?family=Roboto+Slab:wght@700;800&display=swap">
<style>
  :root {
    --card-black: #000000;
    --title-white: #ffffff;
    --accent-orange: #c9772e;
    --accent-tan: #e9a55f;
    --photo-deep: #2b3e4c;
    --photo-mid: #5f7f91;
    --photo-light: #a9c0cc;
    --photo-gold: #d8a626;
  }
  html, body {
    margin: 0;
    padding: 0;
    width: 1200px;
    height: 693px;
    overflow: hidden;
    background: var(--card-black);
  }
  .card {
    position: relative;
    width: 1200px;
    height: 693px;
    display: flex;
    background: var(--card-black);
    font-family: "Roboto Slab", Georgia, serif;
  }
  .studio-photo {
    width: 491px;
    height: 693px;
    flex: none;
    background:
      radial-gradient(ellipse 180px 120px at 190px 170px, rgba(216,166,38,0.75), rgba(216,166,38,0) 70%),
      radial-gradient(ellipse 260px 200px at 300px 300px, var(--photo-light), rgba(169,192,204,0) 75%),
      linear-gradient(160deg, var(--photo-deep) 0%, var(--photo-mid) 45%, var(--photo-deep) 100%);
  }
  .details {
    flex: 1;
    display: flex;
    flex-direction: column;
    align-items: center;
    text-align: center;
    padding-top: 28px;
  }
  .brand-name {
    margin: 0;
    font-size: 92px;
    font-weight: 800;
    line-height: 1.1;
    color: var(--title-white);
    -webkit-text-stroke: 5px var(--accent-orange);
    paint-order: stroke fill;
    letter-spacing: 1px;
  }
  .services, .availability, .web-address {
    margin: 0;
    font-weight: 800;
    color: var(--accent-tan);
    -webkit-text-stroke: 4px var(--title-white);
    paint-order: stroke fill;
  }
  .services {
    margin-top: 44px;
    font-size: 45px;
    line-height: 57px;
  }
  .availability {
    margin-top: 52px;
    font-size: 44px;
  }
  .web-address {
    margin-top: 50px;
    font-size: 40px;
  }
</style>
</head>
<body>
  <main class="card">
    <div class="studio-photo" role="img" aria-label="Photo of a paint-splattered studio floor with a brush, paint tray and tubes of paint"></div>
    <section class="details">
      <h1 class="brand-name">Ka Tivo Art</h1>
      <p class="services">Canvasses, Murals,<br>Vehicles, Cover Art, &amp;<br>Tattoo Design</p>
      <p class="availability">Commissions Available</p>
      <p class="web-address">www.pixelmeet.com/valdipe</p>
    </section>
  </main>
</body>
</html>
```